We need a banner ad design for a company based in Brazil called "Zunaro" (http://www.zunaro-exemplo.com.br), which offers escort services for men. Our main strength and focus is helping people easily search for escorts using mobile devices, by being an mobile optimized repository of escorts which are crawled from many non-mobile optimized sites.

Target Market(s)

Men at all ages (above 18) looking for escorts

Industry/Entity Type

Escort

Requirements
Must have
• Size must be 468x60
The logo must be on white background
Nice to have
• The banner could have an eye-catching animation

The banner could have a small and quick animation showing the usage of the mobile application (like navigating through the application).
Should not have
• If animated then the text should not be split between frames.

```html
<!DOCTYPE html>
<html lang="pt-BR">
<head>
<meta charset="UTF-8">
<title>Zunaro – banners</title>
<link href="https://fonts.googleapis.com/css2?family=Open+Sans:wght@700&display=swap" rel="stylesheet">
<style>
  :root {
    --page-bg: #0c0c0c;
    --brand-red: #9b0d18;
    --logo-bg: #ffffff;
    --text-light: #ffffff;
    --brand-mark: #8a0f18;
    --device-dark: #1a1a1a;
    --device-mid: #5a5a5a;
  }
  html, body {
    margin: 0;
    padding: 0;
    width: 1200px;
    height: 900px;
    overflow: hidden;
    background: var(--page-bg);
    font-family: "Open Sans", Verdana, sans-serif;
  }
  .canvas {
    position: relative;
    width: 1200px;
    height: 900px;
  }
  .banner {
    position: absolute;
    left: 122px;
    width: 960px;
    height: 120px;
    background: var(--brand-red);
    overflow: hidden;
  }
  .banner--catalog { top: 306px; }
  .banner--mobile { top: 508px; }
  .logo-panel {
    position: absolute;
    left: 0;
    top: 0;
    width: 260px;
    height: 120px;
  }
  .logo-panel svg { display: block; }
  .brand-name {
    position: absolute;
    left: 0;
    top: 0;
    width: 240px;
    height: 120px;
    display: flex;
    align-items: center;
    justify-content: center;
    gap: 12px;
    font-size: 38px;
    font-weight: 700;
    color: var(--brand-mark);
    letter-spacing: 1px;
  }
  .brand-dot {
    width: 18px;
    height: 18px;
    border-radius: 50%;
    background: var(--brand-mark);
  }
  .headline {
    position: absolute;
    margin: 0;
    color: var(--text-light);
    font-weight: 700;
    font-size: 33px;
    letter-spacing: 2px;
    line-height: 1;
    white-space: nowrap;
  }
  .headline--first { left: 288px; top: 24px; }
  .headline--second { right: 52px; top: 64px; }
  .headline--tagline { left: 280px; top: 44px; }
  .device-visual {
    position: absolute;
    left: 756px;
    top: 0;
    width: 184px;
    height: 120px;
    background: linear-gradient(120deg, var(--device-dark) 0%, var(--device-mid) 55%, var(--device-dark) 100%);
    border-radius: 10px 10px 0 0;
  }
</style>
</head>
<body>
<div class="canvas">
  <section class="banner banner--catalog">
    <div class="logo-panel">
      <svg width="260" height="120" viewBox="0 0 260 120" aria-hidden="true">
        <path d="M0 0 H258 Q238 58 244 120 H0 Z" fill="var(--logo-bg)"/>
      </svg>
      <div class="brand-name"><span class="brand-dot"></span>Zunaro</div>
    </div>
    <p class="headline headline--first">O maior catálogo</p>
    <p class="headline headline--second">de acompanhantes...</p>
  </section>

  <section class="banner banner--mobile">
    <div class="logo-panel">
      <svg width="260" height="120" viewBox="0 0 260 120" aria-hidden="true">
        <path d="M0 0 H258 Q238 58 244 120 H0 Z" fill="var(--logo-bg)"/>
      </svg>
      <div class="brand-name"><span class="brand-dot"></span>Zunaro</div>
    </div>
    <p class="headline headline--tagline">...na palma da sua mão</p>
    <div class="device-visual" role="img" aria-label="Dois smartphones pretos com telas refletindo luz"></div>
  </section>
</div>
</body>
</html>
```